Liquor Label / Aguardiente

Label design for liquor bottle. Designers may submit multiple submissions.

Product Description:
Name: Luna de Cobre™
Alcohol Category: Aguardiente (which in Spanish most closely translates to “burning water”) – aguardiente is derived from
cane sugar and is a general term for a type of alcoholic spirit in many Central and South America countries.
Taste: A smooth liquor with a comfortable yet spicy finish
Smell: Subtle aroma of spicy jalapeños
Liquid Color: Clear
Bottle Color: Clear
See link for reference - http://www.pellowinery.example/sites/default/files/styles/uc_product_full/public/Vessel_0.jpg?itok=8KqTm2Xw
Closure: Bar top / cork
Bottle Shape/Size: height = 8.67in; diameter of base = 3.70in; diameter of neck = 0.85in

Label may consist of two separate parts (i.e. front and back, front and vertical side), or one continuous label.

Designer has complete freedom with color, font etc. unless otherwise stated below. The label MUST
contain (but is not limited only to) the following text exactly as written in quotes below:
- “Luna de Cobre”
- “Aguardiente”
- “Cane Neutral Spirit with Natural Flavors”
- “35% Alc./Vol.”
- “750 ml”
- “Bottled by QM Spirits, LLC” and “Nashville, TN” - “Government Warning: (1) According to the Surgeon General, women should not drink alcoholic beverages during
pregnancy because of the risk of birth defects. (2) Consumption of alcoholic beverages impairs your ability to
drive a car or operate machinery, and may cause health problems.” (text in previous quotes must be in all
capitalized letters, text must be 2 MM in height and quote must be separated 2MM by all other text)
- Must be dedicated empty space for bar code (approximately 0.75in. height x 1.25in. length)
Updates

Target Market(s)

Label should have mass market appeal.
Age: 21 – 28 years old (primary target market is 21+ year old college students and recent graduates)
Target Market Gender: Both male and female, with emphasis on male
Consumption Focus: Spirit will be consumed typically as a shot, primarily at bars and secondarily off premise (label design will be critical for making our product highly visible behind a bar)
Marketing Theme: South American elements. The official Luna de Cobre mascot is a llama and the incorporation and use of a llama somewhere (however large or small) on the bottle is encourage but by no means required.

Industry/Entity Type

Health

Requirements
Should not have
• Elements that may lead a potential consumer to believe the beverage is a craft liquor or an artisan brand. Please do not include images of peppers.

```html
<!DOCTYPE html>
<html lang="en">
<head>
<meta charset="utf-8">
<title>Luna de Cobre – Aguardiente Label</title>
<link rel="stylesheet" href="https://fonts.googleapis.com/css2?family=Montserrat:wght@200;300&family=Open+Sans:wght@600&display=swap">
<style>
  :root {
    --flame-orange: #d4501c;
    --flame-deep: #b8350f;
    --flame-light: #ee8a4a;
    --label-red: #c0321c;
    --plaque-dark: #262626;
    --plaque-mid: #3a3a3a;
    --ink-white: #ffffff;
    --paper: #ffffff;
  }
  html, body {
    margin: 0;
    padding: 0;
    overflow: hidden;
    background: var(--paper);
  }
  .label {
    position: relative;
    width: 1200px;
    height: 1200px;
    overflow: hidden;
    background: var(--paper);
  }
  .label-art {
    position: absolute;
    inset: 0;
  }
  .label-text {
    position: absolute;
    left: 0;
    width: 1200px;
    text-align: center;
    color: var(--ink-white);
    margin: 0;
    line-height: 1;
  }
  .volume {
    top: 386px;
    font-family: "Montserrat", sans-serif;
    font-weight: 300;
    font-size: 34px;
    letter-spacing: 3px;
  }
  .brand-name {
    top: 462px;
    font-family: "Open Sans", sans-serif;
    font-weight: 600;
    font-size: 72px;
    letter-spacing: 1px;
  }
  .category {
    top: 565px;
    left: 300px;
    width: 586px;
    font-family: "Montserrat", sans-serif;
    font-weight: 300;
    font-size: 19px;
    letter-spacing: 0;
    display: flex;
    justify-content: space-between;
    padding: 0 30px;
    box-sizing: border-box;
  }
  .descriptor {
    top: 648px;
    font-family: "Montserrat", sans-serif;
    font-weight: 300;
    font-size: 33px;
    letter-spacing: 3px;
    line-height: 51px;
  }
  .abv-figure {
    top: 918px;
    left: 489px;
    width: 212px;
    font-family: "Montserrat", sans-serif;
    font-weight: 200;
    font-size: 96px;
  }
  .abv-unit {
    top: 1036px;
    left: 489px;
    width: 212px;
    font-family: "Montserrat", sans-serif;
    font-weight: 300;
    font-size: 37px;
  }
</style>
</head>
<body>
<main class="label">
  <svg class="label-art" width="1200" height="1200" viewBox="0 0 1200 1200">
    <defs>
      <radialGradient id="flameGlow" cx="50%" cy="50%" r="50%">
        <stop offset="0%" stop-color="var(--flame-deep)"/>
        <stop offset="70%" stop-color="var(--flame-orange)"/>
        <stop offset="88%" stop-color="var(--flame-light)" stop-opacity="0.7"/>
        <stop offset="100%" stop-color="var(--flame-light)" stop-opacity="0"/>
      </radialGradient>
      <linearGradient id="plaqueShade" x1="0" y1="0" x2="1" y2="1">
        <stop offset="0%" stop-color="var(--plaque-dark)"/>
        <stop offset="50%" stop-color="var(--plaque-mid)"/>
        <stop offset="100%" stop-color="var(--plaque-dark)"/>
      </linearGradient>
    </defs>

    <ellipse class="flame-wreath" cx="600" cy="600" rx="540" ry="560"
             fill="url(#flameGlow)" role="img"
             aria-label="Wreath of swirling orange flame and smoke around the label"/>

    <circle class="crest-ring" cx="594" cy="196" r="100" fill="var(--paper)"/>
    <circle class="crest-medallion" cx="594" cy="196" r="92" fill="var(--flame-orange)"
            role="img" aria-label="White llama silhouette mascot"/>

    <path class="plaque" role="img" aria-label="Dark plaque with fine diagonal stripes"
          d="M 300 430
             C 300 380 340 360 380 365
             C 440 370 470 340 520 330
             C 560 322 580 340 600 345
             C 620 340 640 322 680 330
             C 730 340 760 370 820 365
             C 860 360 900 380 900 430
             C 890 470 930 490 928 540
             L 928 700
             C 930 750 895 770 900 800
             C 905 840 880 870 840 870
             C 790 870 760 880 720 890
             C 680 900 640 892 600 892
             C 560 892 520 900 480 890
             C 440 880 410 870 360 870
             C 320 870 295 840 300 800
             C 305 770 270 750 272 700
             L 272 540
             C 270 490 310 470 300 430 Z"
          fill="url(#plaqueShade)" stroke="var(--paper)" stroke-width="5"/>

    <rect class="category-band" x="300" y="558" width="586" height="34" fill="var(--label-red)"/>

    <line class="divider" x1="406" y1="792" x2="782" y2="792" stroke="var(--ink-white)" stroke-width="2"/>
    <circle class="divider-medallion" cx="588" cy="794" r="25" fill="var(--flame-orange)"
            stroke="var(--paper)" stroke-width="3" role="img" aria-label="Small llama mascot emblem"/>

    <rect class="abv-frame" x="478" y="904" width="232" height="192" fill="var(--paper)"/>
    <rect class="abv-box" x="489" y="914" width="212" height="174" fill="var(--label-red)"/>
  </svg>

  <p class="label-text volume">750ML</p>
  <h1 class="label-text brand-name">LUNA de COBRE</h1>
  <p class="label-text category">
    <span>A</span><span>G</span><span>U</span><span>A</span><span>R</span><span>D</span><span>I</span><span>E</span><span>N</span><span>T</span><span>E</span>
  </p>
  <p class="label-text descriptor">CANE NEUTRAL SPIRIT<br>WITH NATURAL FLAVORS</p>
  <p class="label-text abv-figure">35%</p>
  <p class="label-text abv-unit">ALC/VOL</p>
</main>
</body>
</html>
```